PowerPoint design MervoSan

We need a PowerPoint set-up based upon our existing logo (see joint file)
Our company is operating in the health care and life science sector. We are mainly focussing on international business

Target Market(s)

International

Industry/Entity Type

health care and life sciences

Requirements
Must have
• Logos as added

```html
<!DOCTYPE html>
<html lang="en">
<head>
<meta charset="utf-8">
<title>MervoSan presentation template</title>
<link rel="stylesheet" href="https://fonts.googleapis.com/css2?family=Poppins:ital,wght@0,400;0,500;0,600;0,700;1,400&display=swap">
<style>
:root{
  --navy:#0b4a86;
  --navy-dark:#083a6b;
  --green:#4cb81a;
  --white:#ffffff;
  --card:#f3f4f6;
  --text:#23344a;
  --muted:#8a96a6;
  --stage:#e3e3e3;
  --photo-a:#dfe5ea;
  --photo-b:#b9c3cc;
}
*{box-sizing:border-box;margin:0;padding:0}
html,body{width:1200px;height:1200px;overflow:hidden}
body{background:var(--stage);font-family:"Poppins",sans-serif;color:var(--text)}
.deck{position:absolute;left:25px;top:144px;display:grid;grid-template-columns:repeat(3,370px);grid-template-rows:repeat(4,208px);gap:20px}
.slide{position:relative;overflow:hidden;background:var(--white);box-shadow:0 6px 18px rgba(0,0,0,.12)}
.slide--hero{grid-column:1/3;grid-row:1/3}
.photo{position:absolute;background:linear-gradient(135deg,var(--photo-a),var(--photo-b))}
.photo--navy{background:linear-gradient(135deg,#2f5f93,#123f70)}
.brand{position:absolute;display:flex;align-items:center;gap:5px;font-weight:600;color:var(--navy)}
.brand__dot{border-radius:50%;background:var(--navy)}
.h{font-weight:700;color:var(--navy);line-height:1.15}
.p{font-size:6px;line-height:1.5;color:var(--text)}
.dash{width:18px;height:2px;background:var(--green)}
.foot{position:absolute;right:10px;bottom:7px;display:flex;align-items:center;gap:5px;font-size:5px;color:var(--muted)}
.foot b{width:11px;height:11px;border-radius:50%;background:var(--green);color:#fff;font-weight:500;display:grid;place-items:center;font-size:5.5px}

/* hero */
.hero__shape{position:absolute;left:0;top:0}
.hero__title{position:absolute;left:56px;top:150px;font-size:44px;font-weight:700;color:#fff;line-height:1.15}
.hero__dash{position:absolute;left:58px;top:270px;width:26px;height:3px;background:var(--green)}
.hero__sub{position:absolute;left:58px;top:286px;font-size:18px;color:#fff}
.hero__blob{position:absolute;right:-60px;bottom:-60px;width:150px;height:150px;border-radius:50%;background:var(--green)}

/* mission */
.mission__title{position:absolute;left:16px;top:26px;font-size:17px}
.mission__band{position:absolute;left:0;top:62px;width:200px;height:40px;background:var(--navy);display:flex;align-items:center;gap:10px;padding-left:16px;color:#fff;font-size:8px;font-weight:600}
.icon-disc{width:22px;height:22px;border-radius:50%;background:var(--green);display:grid;place-items:center}
.mission__body{position:absolute;left:22px;top:114px;width:170px}
.mission__body p+p{margin-top:5px}

/* services */
.services__top{position:absolute;left:0;top:0;width:100%;height:96px}
.services__title{position:absolute;right:16px;top:14px;font-size:16px;color:#fff}
.services__cards{position:absolute;left:14px;top:62px;display:flex;gap:10px}
.svc{width:106px;height:118px;background:#fff;border-radius:4px;box-shadow:0 3px 10px rgba(0,0,0,.12);text-align:center;padding:26px 8px 0;position:relative}
.svc__ring{position:absolute;left:50%;top:-16px;margin-left:-16px;width:32px;height:32px;border-radius:50%;border:3px solid var(--green);background:#eceff2;display:grid;place-items:center}
.svc__title{font-size:7.5px;font-weight:600;color:var(--navy)}
.svc .dash{margin:5px auto;width:12px;height:1px;background:#ccd}
.svc .p{font-size:5.3px}

/* section */
.section__title{position:absolute;left:30px;top:72px;font-size:20px;color:#fff;font-weight:700}
.section__dash{position:absolute;left:32px;top:104px}
.section__sub{position:absolute;left:32px;top:114px;font-size:10px;color:#fff}

/* teams */
.teams__title{position:absolute;left:16px;top:14px;font-size:15px}
.teams__grid{position:absolute;left:16px;top:46px;display:grid;grid-template-columns:repeat(3,106px);gap:8px}
.member{background:var(--card);padding:8px;height:68px}
.member__head{display:flex;align-items:center;gap:5px}
.member__avatar{width:14px;height:14px;border-radius:50%;background:var(--navy);position:relative}
.member__avatar::after{content:"";position:absolute;left:4.5px;top:3px;width:5px;height:5px;border-radius:50%;background:#fff}
.member__name{font-size:6.5px;font-weight:600;color:var(--navy);line-height:1.1}
.member__role{font-size:5.5px;font-style:italic;color:var(--navy)}
.member__line{height:1px;background:var(--green);margin:4px 0}
.member .p{font-size:4.6px;line-height:1.4}

/* process */
.process__title{position:absolute;left:16px;top:14px;font-size:15px}
.process__svg{position:absolute;left:0;top:0}
.step{position:absolute;width:104px}
.step__title{font-size:8px;font-weight:600;color:var(--navy)}
.step .dash{width:12px;height:1px;margin:3px 0}
.step .p{font-size:5.2px}

/* chart */
.chart__side{position:absolute;left:0;top:0;width:110px;height:100%;background:var(--navy)}
.chart__title{position:absolute;left:14px;top:30px;font-size:13px;color:#fff;opacity:.9}
.chart__dash{position:absolute;left:14px;top:68px}
.chart__table{position:absolute;left:62px;top:18px}
.chart__legend{position:absolute;left:120px;bottom:22px;display:flex;gap:18px;font-size:4.6px;color:var(--text)}
.chart__legend span{display:flex;align-items:center;gap:3px}
.chart__legend i{width:6px;height:6px;display:inline-block}

/* contact */
.contact__title{position:absolute;left:196px;top:62px;font-size:15px;color:#fff}
.contact__dash{position:absolute;left:198px;top:86px}
.contact__body{position:absolute;left:198px;top:96px;width:130px;color:#fff;font-size:6.5px;line-height:1.5}
</style>
</head>
<body>
<main class="deck">

  <!-- Title slide -->
  <section class="slide slide--hero">
    <div class="photo" style="left:300px;top:0;width:460px;height:436px" role="img" aria-label="Photo of a doctor in a white coat holding a stethoscope"></div>
    <div class="hero__blob"></div>
    <svg class="hero__shape" width="760" height="436" viewBox="0 0 760 436" aria-hidden="true">
      <path d="M0 56 H390 A190 190 0 0 1 390 436 H0 Z" fill="var(--navy)"/>
      <path d="M0 70 H390 A176 176 0 0 1 390 422 H0" fill="none" stroke="#fff" stroke-width="2.5"/>
    </svg>
    <h1 class="hero__title">Presentation title<br>here</h1>
    <div class="hero__dash"></div>
    <p class="hero__sub">Type your subtitle here</p>
    <div class="brand" style="right:40px;top:30px;font-size:20px"><span class="brand__dot" style="width:22px;height:22px"></span>MervoSan</div>
  </section>

  <!-- Mission -->
  <section class="slide">
    <h2 class="h mission__title">Our Mission</h2>
    <div class="photo" style="left:200px;top:0;width:170px;height:190px;border-bottom-left-radius:26px" role="img" aria-label="Photo of doctors discussing at a desk with a laptop"></div>
    <div class="mission__band">
      <span class="icon-disc"><svg width="10" height="10" viewBox="0 0 10 10"><rect x="3" y="1" width="4" height="8" rx="1" fill="none" stroke="#fff" stroke-width="1.2"/><line x1="3" y1="5" x2="7" y2="5" stroke="#fff" stroke-width="1"/></svg></span>
      Type your mission here
    </div>
    <div class="mission__body p">
      <p>Lorem ipsum dolor sit amet, consectetur adipiscing elit, sed do eiusmod tempor incididunt ut labore et dolore magna aliqua.</p>
      <p>Ut enim ad minim veniam, quis nostrud exercitation ullamco laboris nisi ut aliquip ex ea commodo consequat. Duis aute irure dolor in.</p>
    </div>
  </section>

  <!-- Services -->
  <section class="slide">
    <div class="photo photo--navy services__top" role="img" aria-label="Blue-tinted photo of medical staff at work"></div>
    <h2 class="h services__title">Our Services</h2>
    <div class="services__cards">
      <div class="svc">
        <span class="svc__ring"><svg width="14" height="14" viewBox="0 0 14 14"><path d="M10 2 L12 4 L5 11 L3 11 L3 9 Z" fill="var(--green)"/></svg></span>
        <div class="svc__title">Service title here</div><div class="dash"></div>
        <p class="p">Lorem ipsum dolor sit amet, consectetur adipiscing elit, sed do eiusmod tempor incididunt ut labore et dolore magna sit aliqua.</p>
      </div>
      <div class="svc">
        <span class="svc__ring"><svg width="14" height="14" viewBox="0 0 14 14" fill="none" stroke="var(--green)" stroke-width="1.3"><circle cx="5" cy="5" r="2.5"/><circle cx="10" cy="7" r="2.5"/><circle cx="5" cy="10.5" r="2.5"/></svg></span>
        <div class="svc__title">Service title here</div><div class="dash"></div>
        <p class="p">Lorem ipsum dolor sit amet, consectetur adipiscing elit, sed do eiusmod tempor incididunt ut labore et dolore magna sit aliqua.</p>
      </div>
      <div class="svc">
        <span class="svc__ring"><svg width="14" height="14" viewBox="0 0 14 14"><circle cx="7" cy="7" r="6" fill="var(--green)"/><path d="M7 3.5V10.5M3.5 7H10.5" stroke="#fff" stroke-width="2"/></svg></span>
        <div class="svc__title">Service title here</div><div class="dash"></div>
        <p class="p">Lorem ipsum dolor sit amet, consectetur adipiscing elit, sed do eiusmod tempor incididunt ut labore et dolore magna sit aliqua.</p>
      </div>
    </div>
  </section>

  <!-- Teams -->
  <section class="slide">
    <h2 class="h teams__title">Our teams</h2>
    <div class="teams__grid">
      <div class="member"><div class="member__head"><span class="member__avatar"></span><div><div class="member__name">Name here</div><div class="member__role">Position here</div></div></div><div class="member__line"></div><p class="p">Lorem ipsum dolor sit amet, consectetur adipiscing elit, sed do eiusmod tempor incididunt ut labore aliqua.</p></div>
      <div class="member"><div class="member__head"><span class="member__avatar"></span><div><div class="member__name">Name here</div><div class="member__role">Position here</div></div></div><div class="member__line"></div><p class="p">Lorem ipsum dolor sit amet, consectetur adipiscing elit, sed do eiusmod tempor incididunt ut labore aliqua.</p></div>
      <div class="member"><div class="member__head"><span class="member__avatar"></span><div><div class="member__name">Name here</div><div class="member__role">Position here</div></div></div><div class="member__line"></div><p class="p">Lorem ipsum dolor sit amet, consectetur adipiscing elit, sed do eiusmod tempor incididunt ut labore aliqua.</p></div>
      <div class="member"><div class="member__head"><span class="member__avatar"></span><div><div class="member__name">Name here</div><div class="member__role">Position here</div></div></div><div class="member__line"></div><p class="p">Lorem ipsum dolor sit amet, consectetur adipiscing elit, sed do eiusmod tempor incididunt ut labore aliqua.</p></div>
      <div class="member"><div class="member__head"><span class="member__avatar"></span><div><div class="member__name">Name here</div><div class="member__role">Position here</div></div></div><div class="member__line"></div><p class="p">Lorem ipsum dolor sit amet, consectetur adipiscing elit, sed do eiusmod tempor incididunt ut labore aliqua.</p></div>
      <div class="member"><div class="member__head"><span class="member__avatar"></span><div><div class="member__name">Name here</div><div class="member__role">Position here</div></div></div><div class="member__line"></div><p class="p">Lorem ipsum dolor sit amet, consectetur adipiscing elit, sed do eiusmod tempor incididunt ut labore aliqua.</p></div>
    </div>
  </section>

  <!-- Process -->
  <section class="slide">
    <h2 class="h process__title">Process</h2>
    <svg class="process__svg" width="370" height="208" viewBox="0 0 370 208" aria-hidden="true">
      <path d="M20 78 H344" stroke="var(--green)" stroke-width="2.5"/>
      <path d="M336 72 L346 78 L336 84" fill="none" stroke="var(--green)" stroke-width="2.5"/>
      <g stroke="var(--green)" stroke-width="2.5" fill="var(--navy)"><circle cx="36" cy="78" r="13"/><circle cx="150" cy="78" r="13"/><circle cx="264" cy="78" r="13"/></g>
      <g fill="none" stroke="#fff" stroke-width="1.2"><path d="M32 74 H40 M32 78 H40 M32 82 H38"/><circle cx="147" cy="75" r="2.5"/><circle cx="153" cy="78" r="2.5"/><circle cx="147" cy="81" r="2.5"/><circle cx="264" cy="78" r="5.5"/><path d="M264 75 V81 M261 78 H267"/></g>
    </svg>
    <div class="step" style="left:22px;top:100px"><div class="step__title">Process 1</div><div class="dash"></div><p class="p">Lorem ipsum dolor sit amet, consectetur adipiscing elit, sed do eiusmod tempor incididunt ut labore et dolore magna aliqua. Ut enim ad minim veniam</p></div>
    <div class="step" style="left:136px;top:100px"><div class="step__title">Process 2</div><div class="dash"></div><p class="p">Lorem ipsum dolor sit amet, consectetur adipiscing elit, sed do eiusmod tempor incididunt ut labore et dolore magna aliqua. Ut enim ad minim veniam</p></div>
    <div class="step" style="left:250px;top:100px"><div class="step__title">Process 3</div><div class="dash"></div><p class="p">Lorem ipsum dolor sit amet, consectetur adipiscing elit, sed do eiusmod tempor incididunt ut labore et dolore magna aliqua. Ut enim ad minim veniam</p></div>
    <div class="brand" style="left:16px;bottom:8px;font-size:7px"><span class="brand__dot" style="width:8px;height:8px"></span>MervoSan</div>
    <div class="foot">www.mervosan.com <b>6</b></div>
  </section>

  <!-- Chart report -->
  <section class="slide">
    <div class="chart__side"></div>
    <h2 class="chart__title h" style="color:#fff">Chart<br>Report</h2>
    <div class="dash chart__dash"></div>
    <svg class="chart__table" width="296" height="160" viewBox="0 0 296 160" aria-label="Gantt chart of project tasks from January to April">
      <rect width="296" height="160" rx="4" fill="#fff"/>
      <rect width="296" height="16" fill="var(--navy-dark)"/>
      <g font-family="Poppins,sans-serif" font-size="6" fill="#fff"><text x="8" y="11">Task Name</text><text x="86" y="11">Jan</text><text x="138" y="11">Feb</text><text x="190" y="11">Mar</text><text x="242" y="11">Apr</text></g>
      <rect x="0" y="16" width="78" height="120" fill="var(--card)"/>
      <g font-family="Poppins,sans-serif" font-size="6" font-weight="600" fill="var(--text)"><text x="8" y="32">Planning</text><text x="8" y="52">Research</text><text x="8" y="72">Design</text><text x="8" y="92">Implementation</text><text x="8" y="112">Follow up</text></g>
      <g stroke="#e6e8ec" stroke-width=".6"><path d="M78 16V136M130 16V136M182 16V136M234 16V136M0 40H296M0 60H296M0 80H296M0 100H296M0 120H296"/></g>
      <rect x="82" y="20" width="30" height="7" fill="var(--green)"/>
      <rect x="112" y="30" width="12" height="7" fill="#d3d6da"/><rect x="124" y="30" width="40" height="7" fill="var(--green)"/>
      <rect x="164" y="48" width="28" height="7" fill="var(--navy)"/>
      <rect x="192" y="66" width="48" height="7" fill="var(--green)"/>
      <rect x="230" y="86" width="50" height="7" fill="var(--navy)"/>
    </svg>
    <div class="chart__legend"><span><i style="background:#d3d6da"></i>Lorem ipsum dolor sit amet</span><span><i style="background:var(--green)"></i>Lorem ipsum dolor sit amet</span><span><i style="background:var(--navy)"></i>Lorem ipsum dolor sit amet</span></div>
    <div class="foot">www.mervosan.com <b>7</b></div>
  </section>

  <!-- Section title -->
  <section class="slide">
    <div class="photo photo--navy" style="inset:0" role="img" aria-label="Blue-tinted photo of a doctor writing on a clipboard"></div>
    <h2 class="section__title">Section title here</h2>
    <div class="dash section__dash"></div>
    <p class="section__sub">Subtitle here</p>
  </section>

  <!-- Contact -->
  <section class="slide">
    <div class="photo" style="inset:0" role="img" aria-label="Photo of a medical professional"></div>
    <svg style="position:absolute;left:0;top:0" width="370" height="208" viewBox="0 0 370 208" aria-hidden="true">
      <path d="M150 208 L214 20 Q222 0 244 0 H370 V208 Z" fill="var(--navy)"/>
      <path d="M314 208 L346 110 Q356 78 340 50" fill="none" stroke="#fff" stroke-width="1.5"/>
      <path d="M300 208 Q316 160 360 170 L370 172 V208 Z" fill="var(--green)"/>
    </svg>
    <h2 class="contact__title h" style="color:#fff;left:200px">Contact us</h2>
    <div class="dash contact__dash"></div>
    <p class="contact__body">Lorem ipsum dolor sit amet, consectetur adipiscing elit, sed do eiusmod tempor incididunt ut labore et dolore magna aliqua.</p>
  </section>

  <!-- Title slide, circle variant -->
  <section class="slide">
    <div class="photo" style="inset:0" role="img" aria-label="Photo of a doctor in a white coat holding a stethoscope"></div>
    <div style="position:absolute;right:-24px;bottom:-24px;width:70px;height:70px;border-radius:50%;background:var(--green)"></div>
    <svg style="position:absolute;left:0;top:0" width="370" height="208" viewBox="0 0 370 208" aria-hidden="true">
      <circle cx="70" cy="104" r="116" fill="var(--navy)"/>
      <circle cx="70" cy="104" r="106" fill="none" stroke="#fff" stroke-width="1.5"/>
    </svg>
    <h2 style="position:absolute;left:20px;top:68px;font-size:18px;font-weight:700;color:#fff;line-height:1.2">Presentation<br>title here</h2>
    <div class="dash" style="position:absolute;left:22px;top:120px"></div>
    <p style="position:absolute;left:22px;top:128px;font-size:7px;color:#fff">Type your subtitle here</p>
    <div class="brand" style="right:16px;top:14px;font-size:10px"><span class="brand__dot" style="width:11px;height:11px"></span>MervoSan</div>
  </section>

</main>
</body>
</html>
```